Natural Cosmetics need a Packaging Design

We need a PACKAGING design for labels on hand/body wash bottles and soap paper boxes.
We target at high end markets.
We expect a contemporary and trendy design.
We don't need a separate logo. The brand name "Va Mirel" acts as the logo.
We want a modern and classic font for "Va Mirel".
Please see attached pictures for packaging samples.

Industry/Entity Type

Cosmetics

Requirements
Should not have
• a separate logo from the brand name

```html
<!DOCTYPE html>
<html lang="en">
<head>
<meta charset="utf-8">
<title>Va Mirel — Packaging Labels</title>
<link rel="stylesheet" href="https://fonts.googleapis.com/css2?family=Cormorant+Garamond:wght@700&family=Josefin+Sans:wght@700&display=swap">
<style>
  :root {
    --paper: #ffffff;
    --ink: #3f3a7d;
    --frame: #4a437e;
    --band-blue: #5866a8;
    --label-teal: #3d8aa0;
    --label-green: #12aa5a;
    --band-green: #0a9f4c;
    --tag-light: #e4ebcf;
    --tag-green: #a9d184;
    --dieline: #a9a9a9;
    --pearl-1: #fbf6fb;
    --pearl-2: #f1dbe8;
    --pearl-3: #dde6f5;
    --motif-peach: #f0b08c;
    --motif-lilac: #b9b2e0;
  }
  html, body {
    margin: 0;
    width: 1200px;
    height: 1000px;
    overflow: hidden;
    background: var(--paper);
  }
  .canvas { position: relative; width: 1200px; height: 1000px; }
  .artwork { position: absolute; inset: 0; }
  .brand-serif { font-family: "Cormorant Garamond", Georgia, serif; font-weight: 700; fill: var(--ink); }
  .brand-sans { font-family: "Josefin Sans", Arial, sans-serif; font-weight: 700; fill: var(--ink); }
  .dieline { fill: var(--paper); stroke: var(--dieline); stroke-width: 1.4; }
</style>
</head>
<body>
<div class="canvas">
<svg class="artwork" width="1200" height="1000" viewBox="0 0 1200 1000" xmlns="http://www.w3.org/2000/svg">
  <defs>
    <linearGradient id="pearl" x1="0" y1="0" x2="1" y2="0">
      <stop offset="0" stop-color="var(--pearl-2)"/>
      <stop offset="0.35" stop-color="var(--pearl-1)"/>
      <stop offset="0.65" stop-color="var(--pearl-3)"/>
      <stop offset="1" stop-color="var(--pearl-2)"/>
    </linearGradient>
    <linearGradient id="label-fade" x1="0" y1="0" x2="0" y2="1">
      <stop offset="0" stop-color="var(--band-blue)"/>
      <stop offset="0.45" stop-color="var(--label-teal)"/>
      <stop offset="1" stop-color="var(--label-green)"/>
    </linearGradient>
    <radialGradient id="motif" cx="0.5" cy="0.5" r="0.5">
      <stop offset="0" stop-color="var(--motif-lilac)" stop-opacity="0.85"/>
      <stop offset="0.55" stop-color="var(--motif-peach)" stop-opacity="0.55"/>
      <stop offset="1" stop-color="var(--motif-peach)" stop-opacity="0"/>
    </radialGradient>
    <linearGradient id="tag-fade" x1="0" y1="0" x2="0" y2="1">
      <stop offset="0" stop-color="var(--tag-light)"/>
      <stop offset="1" stop-color="var(--tag-green)"/>
    </linearGradient>
  </defs>

  <!-- Tall bottle, blank tag -->
  <g class="bottle">
    <rect x="150" y="42" width="110" height="10" fill="url(#pearl)"/>
    <rect x="178" y="35" width="57" height="68" fill="url(#pearl)"/>
    <rect x="165" y="100" width="80" height="48" fill="url(#pearl)"/>
    <rect x="137" y="147" width="131" height="328" rx="12" fill="url(#pearl)"/>
    <rect x="137" y="160" width="131" height="295" fill="url(#label-fade)"/>
    <rect x="137" y="160" width="131" height="16" fill="var(--band-blue)"/>
    <rect x="137" y="430" width="131" height="25" fill="var(--band-green)"/>
    <rect x="137" y="177" width="131" height="1.5" fill="#cfd3e6"/>
    <rect x="137" y="428" width="131" height="1.5" fill="#cfe6d6"/>
    <ellipse role="img" aria-label="Flowing botanical line pattern in peach and lilac" cx="205" cy="315" rx="70" ry="130" fill="url(#motif)"/>
    <rect class="blank-tag" x="146" y="365" width="115" height="57" fill="var(--tag-light)"/>
  </g>

  <!-- Tall bottle, brand tag -->
  <g class="bottle">
    <rect x="305" y="42" width="110" height="10" fill="url(#pearl)"/>
    <rect x="331" y="35" width="57" height="68" fill="url(#pearl)"/>
    <rect x="322" y="100" width="80" height="48" fill="url(#pearl)"/>
    <rect x="295" y="147" width="132" height="328" rx="12" fill="url(#pearl)"/>
    <rect x="295" y="160" width="132" height="295" fill="url(#label-fade)"/>
    <rect x="295" y="160" width="132" height="16" fill="var(--band-blue)"/>
    <rect x="295" y="430" width="132" height="25" fill="var(--band-green)"/>
    <rect x="295" y="177" width="132" height="1.5" fill="#cfd3e6"/>
    <rect x="295" y="428" width="132" height="1.5" fill="#cfe6d6"/>
    <ellipse role="img" aria-label="Flowing botanical line pattern in peach and lilac" cx="362" cy="315" rx="70" ry="130" fill="url(#motif)"/>
    <rect x="313" y="265" width="96" height="35" fill="var(--tag-light)" stroke="var(--frame)" stroke-width="2"/>
    <text class="brand-serif" x="361" y="289" font-size="17" text-anchor="middle">Va Mirel</text>
  </g>

  <!-- Short bottle, blank tag -->
  <g class="bottle">
    <rect x="150" y="545" width="85" height="9" fill="url(#pearl)"/>
    <rect x="178" y="540" width="33" height="62" fill="url(#pearl)"/>
    <rect x="165" y="600" width="60" height="24" fill="url(#pearl)"/>
    <rect x="122" y="622" width="143" height="208" rx="10" fill="url(#pearl)"/>
    <rect x="122" y="628" width="143" height="194" fill="url(#label-fade)"/>
    <rect x="122" y="628" width="143" height="12" fill="var(--band-blue)"/>
    <rect x="122" y="800" width="143" height="22" fill="var(--band-green)"/>
    <rect x="122" y="641" width="143" height="1.5" fill="#cfd3e6"/>
    <rect x="122" y="799" width="143" height="1.5" fill="#cfe6d6"/>
    <ellipse role="img" aria-label="Flowing botanical line pattern in peach and lilac" cx="195" cy="725" rx="72" ry="90" fill="url(#motif)"/>
    <rect class="blank-tag" x="155" y="757" width="82" height="41" fill="var(--tag-light)"/>
  </g>

  <!-- Short bottle, brand tag -->
  <g class="bottle">
    <rect x="328" y="545" width="85" height="9" fill="url(#pearl)"/>
    <rect x="356" y="540" width="33" height="62" fill="url(#pearl)"/>
    <rect x="343" y="600" width="60" height="24" fill="url(#pearl)"/>
    <rect x="300" y="622" width="143" height="208" rx="10" fill="url(#pearl)"/>
    <rect x="300" y="628" width="143" height="194" fill="url(#label-fade)"/>
    <rect x="300" y="628" width="143" height="12" fill="var(--band-blue)"/>
    <rect x="300" y="800" width="143" height="22" fill="var(--band-green)"/>
    <rect x="300" y="641" width="143" height="1.5" fill="#cfd3e6"/>
    <rect x="300" y="799" width="143" height="1.5" fill="#cfe6d6"/>
    <ellipse role="img" aria-label="Flowing botanical line pattern in peach and lilac" cx="373" cy="725" rx="72" ry="90" fill="url(#motif)"/>
    <rect x="328" y="713" width="90" height="35" fill="var(--tag-light)" stroke="var(--frame)" stroke-width="2"/>
    <text class="brand-serif" x="373" y="737" font-size="17" text-anchor="middle">Va Mirel</text>
  </g>

  <!-- Brand name tag studies -->
  <g class="tag-study">
    <rect x="514" y="114" width="189" height="74" fill="#fff" stroke="var(--frame)" stroke-width="2"/>
    <rect x="520" y="120" width="177" height="62" fill="url(#tag-fade)"/>
    <text class="brand-serif" x="608" y="164" font-size="36" text-anchor="middle">Va Mirel</text>
  </g>
  <g class="tag-study">
    <rect x="514" y="201" width="189" height="72" fill="#fff" stroke="var(--frame)" stroke-width="2"/>
    <rect x="520" y="207" width="177" height="60" fill="var(--tag-light)"/>
    <text class="brand-serif" x="608" y="250" font-size="36" text-anchor="middle">Va Mirel</text>
  </g>
  <g class="tag-study">
    <rect x="515" y="305" width="189" height="72" fill="#fff" stroke="var(--frame)" stroke-width="2"/>
    <rect x="521" y="311" width="177" height="60" fill="url(#tag-fade)"/>
    <text class="brand-sans" x="609" y="353" font-size="30" text-anchor="middle">Va Mirel</text>
  </g>
  <g class="tag-study">
    <rect x="515" y="391" width="189" height="72" fill="#fff" stroke="var(--frame)" stroke-width="2"/>
    <rect x="521" y="397" width="177" height="60" fill="var(--tag-light)"/>
    <text class="brand-sans" x="609" y="439" font-size="30" text-anchor="middle">Va Mirel</text>
  </g>

  <!-- Soap box dieline -->
  <g class="soap-box">
    <rect class="dieline" x="860" y="343" width="144" height="147"/>
    <path class="dieline" d="M860 465 H725 Q715 465 715 475 V488 L695 498 V625 L715 635 V648 Q715 658 725 658 H850 L860 632 V490 Z"/>
    <path class="dieline" d="M716 488 H860 M716 635 H860"/>
    <path class="dieline" d="M1004 465 H1140 Q1150 465 1150 475 V488 L1170 498 V625 L1150 635 V648 Q1150 658 1140 658 H1014 L1004 632 V490 Z"/>
    <path class="dieline" d="M1004 488 H1150 M1004 635 H1150"/>
    <rect class="dieline" x="860" y="632" width="144" height="146"/>
    <path class="dieline" d="M860 920 L866 936 Q868 942 876 942 H988 Q996 942 998 936 L1004 920 Z"/>

    <rect x="860" y="490" width="144" height="142" fill="url(#label-fade)"/>
    <rect x="860" y="490" width="144" height="8" fill="var(--band-blue)"/>
    <rect x="860" y="620" width="144" height="12" fill="var(--band-green)"/>
    <ellipse role="img" aria-label="Flowing botanical line pattern in peach and lilac" cx="930" cy="565" rx="68" ry="70" fill="url(#motif)"/>
    <rect x="891" y="536" width="80" height="30" fill="var(--tag-light)" stroke="var(--frame)" stroke-width="2"/>
    <text class="brand-serif" x="931" y="556" font-size="15" text-anchor="middle">Va Mirel</text>

    <rect x="860" y="778" width="144" height="142" fill="url(#label-fade)"/>
    <rect x="860" y="778" width="144" height="8" fill="var(--band-blue)"/>
    <rect x="860" y="906" width="144" height="14" fill="var(--band-green)"/>
    <ellipse role="img" aria-label="Flowing botanical line pattern in peach and lilac" cx="930" cy="850" rx="68" ry="70" fill="url(#motif)"/>
  </g>
</svg>
</div>
</body>
</html>
```